Need a one sheet capability statement for my consulting company

We need a slick capability statement for an Aviation Consulting company. We provide Air Traffic Control, Aerospace Services and Enterprise IT Support for the Aviation community. Our customers are ORVEL, Airlines, Airports, and the Coastal Flight Directorate. We would to have a design that uses the scheme in our logo, and look a bit slick and very professional and impressive. The final design should clearly community that we are Aviation Experts.

Target Market(s)

Airlines, Coastal Flight Directorate, ORVEL, Air Traffic Control, Airports

Industry/Entity Type

Aviation

Colors
86cae7
33a6d7
85cae6

Requirements
Must have
• Nice colors that blend in well with our Logo. Easy to read capability document. Elegant and communicate professionalism
Nice to have
• Slick colors preferably sky blue, but open to whatever color the designers thinks will look great.

```html
<!DOCTYPE html>
<html lang="en">
<head>
<meta charset="utf-8">
<title>Skyvale Consulting Group – Capability Statement</title>
<link href="https://fonts.googleapis.com/css2?family=Lato:wght@400;700&display=swap" rel="stylesheet">
<style>
:root{
  --sky:#33a6d7;
  --sky-light:#86cae7;
  --slate:#5f6064;
  --slate-dark:#3f4044;
  --ink:#333538;
  --band:#d2d3d5;
  --band-light:#e3e4e6;
  --paper:#ffffff;
  --stage:#ececec;
}
*{margin:0;padding:0;box-sizing:border-box}
html,body{width:1200px;height:903px;overflow:hidden}
body{background:var(--stage);font-family:'Lato',sans-serif;color:var(--ink);position:relative}
.page{position:absolute;top:146px;width:510px;height:659px;background:var(--paper);overflow:hidden;box-shadow:0 2px 10px rgba(0,0,0,.18)}
.page--front{left:57px}
.page--back{left:633px}
.hero{position:absolute;left:0;top:0;width:510px;background:linear-gradient(180deg,#d6e6f2 0%,#b9d1e3 45%,#5f7486 72%,#c9dbe8 100%)}
.page--front .hero{height:238px}
.page--back .hero{height:258px}
.brand{position:absolute;top:0;height:86px;background:var(--paper);display:flex;flex-direction:column;justify-content:center;align-items:flex-end;color:#58595b;font-weight:700;padding-right:26px}
.page--front .brand{left:0;width:262px;clip-path:polygon(0 0,100% 0,95% 100%,0 100%)}
.page--back .brand{right:0;width:276px;clip-path:polygon(0 0,100% 0,100% 100%,5% 100%)}
.brand__name{font-size:36px;letter-spacing:1px;line-height:1;display:flex;align-items:center;gap:8px}
.brand__dot{width:12px;height:12px;border-radius:50%;background:var(--sky)}
.brand__sub{font-size:9.5px;letter-spacing:.5px;margin-top:6px}
.band{position:absolute;left:0;top:238px;width:510px;height:162px;background:var(--band)}
.band__left{position:absolute;left:0;top:0;width:255px;height:162px;background:var(--band-light)}
.band__head{position:absolute;top:0;height:24px;font-size:9.5px;font-weight:700;line-height:24px;color:var(--ink)}
.band__headrow{position:absolute;left:0;top:0;width:510px;height:24px;background:#cdced0;border-bottom:1px solid #bdbec0}
.tag{position:absolute;background:var(--sky);color:#fff;font-size:7.5px;font-weight:700;padding:1px 3px;line-height:9px}
.val{position:absolute;font-size:8px;line-height:10px;color:var(--ink)}
.val--lg{font-size:10px}
.panel{position:absolute;background:var(--sky);color:#fff}
.tab{position:absolute;background:var(--slate);color:#fff;font-size:11px;font-weight:700;line-height:24px;padding-left:12px;clip-path:polygon(0 0,92% 0,100% 50%,92% 100%,0 100%)}
.svc-head{position:absolute;font-size:9.5px;font-weight:700;color:#fff;display:flex;align-items:center;gap:8px}
.svc-item,.list-item{position:absolute;font-size:7.8px;line-height:9.5px;padding-left:14px}
.svc-item{color:#fff}
.svc-item::before,.list-item::before{content:"";position:absolute;left:0;top:2px;width:5px;height:5px;border:1px solid currentColor;opacity:.8}
.list-item{color:var(--ink)}
.list-item::before{border-color:var(--sky)}
.sec-head{position:absolute;height:13px;border-bottom:1px solid #9a9b9e}
.sec-head span{display:inline-block;position:relative;background:var(--sky);color:#fff;font-size:9px;font-weight:700;line-height:12px;padding:0 4px}
.sec-head span::after{content:"";position:absolute;right:-7px;top:0;width:4px;height:13px;background:var(--slate-dark);transform:skewX(-25deg)}
.overview{position:absolute;left:248px;top:437px;width:237px;font-size:7.6px;line-height:10px;text-align:justify}
.ref{position:absolute;left:47px;width:150px;color:#fff;font-size:9.5px;line-height:12px}
.ref b{font-weight:700}
.ref__mail{display:flex;align-items:center;gap:5px;margin-top:4px}
.mail-ico{width:9px;height:6px;border:1px solid #fff}
.photo{position:absolute;background:linear-gradient(180deg,#7fc3e6 0%,#3ca9dc 55%,#2a8fc2 100%)}
.list-item.sm{font-size:6.9px;line-height:8.4px}
.footer{position:absolute;left:0;bottom:0;width:510px;height:27px;background:var(--slate);color:#fff;font-size:7.4px;display:flex;align-items:center}
.footer__info{padding-left:20px;display:flex;align-items:center;gap:5px;white-space:nowrap}
.footer__sep{width:1px;height:10px;background:#fff;opacity:.7}
.footer__phone{position:absolute;right:0;top:0;height:27px;width:128px;background:var(--sky);clip-path:polygon(8% 0,100% 0,100% 100%,0 100%);display:flex;align-items:center;gap:6px;padding-left:18px;font-size:10px;font-weight:700}
</style>
</head>
<body>

<section class="page page--front">
  <div class="hero" role="img" aria-label="Silhouettes of business travellers meeting and walking past airport terminal windows with an airliner flying overhead"></div>
  <div class="brand">
    <div class="brand__name"><span class="brand__dot"></span>SKYVALE</div>
    <div class="brand__sub">CONSULTING GROUP</div>
  </div>

  <div class="band">
    <div class="band__left"></div>
    <div class="band__headrow"></div>
    <div class="band__head" style="left:25px">Corporate Information</div>
    <div class="band__head" style="left:312px">MBE/DBE/SBE Certified</div>

    <div class="tag" style="left:25px;top:36px">President:</div><div class="val" style="left:73px;top:34px;font-size:9.5px">Martin L. Okafor</div>
    <div class="tag" style="left:25px;top:53px">Phone:</div><div class="val" style="left:73px;top:53px">(555) 014-2290</div>
    <div class="tag" style="left:25px;top:71px">Email:</div><div class="val" style="left:73px;top:71px">martin.okafor@skyvaleconsulting.com</div>
    <div class="tag" style="left:25px;top:89px">Website:</div><div class="val" style="left:73px;top:89px">www.skyvaleconsulting.com</div>
    <div class="tag" style="left:25px;top:107px">Certifications:</div><div class="val" style="left:86px;top:107px;width:160px">Sprint Lead, Lean Process Greenbelt, SVCM, DEFAF, PFMN, EAF, TeamDock, CSSPX, Corvane, DataLedger</div>
    <div class="tag" style="left:25px;top:141px">Tools:</div><div class="val" style="left:56px;top:142px">TRAXIS, Model Architect, MAPPA, TeamDock</div>

    <div class="tag" style="left:259px;top:36px">Primary NAICs Codes</div>
    <div class="val" style="left:283px;top:48px">541511</div><div class="val" style="left:355px;top:48px">541611</div><div class="val" style="left:421px;top:48px">488111</div>
    <div class="val" style="left:283px;top:67px">541512</div><div class="val" style="left:355px;top:67px">541330</div><div class="val" style="left:421px;top:67px">561110</div>
    <div class="tag" style="left:259px;top:94px">PSC Codes</div>
    <div class="val" style="left:261px;top:108px">R408 R425 U008 U009</div><div class="val" style="left:374px;top:108px">D302 D307 D308 D310 D314</div>
    <div class="tag" style="left:261px;top:134px">D-U-N-S:</div>
    <div class="tag" style="left:374px;top:134px">Cage Code:</div>
    <div class="val val--lg" style="left:263px;top:147px">061532874</div>
    <div class="val val--lg" style="left:376px;top:147px">4QX81</div>
  </div>

  <div class="panel" style="left:26px;top:400px;width:194px;height:232px"></div>
  <div class="tab" style="left:15px;top:405px;width:150px;height:24px">SERVICE OFFERINGS</div>

  <div class="svc-head" style="left:37px;top:434px">
    <svg width="14" height="10" viewBox="0 0 14 10" aria-hidden="true"><rect x="2" y="1" width="10" height="6" fill="none" stroke="#fff" stroke-width="1.2"/><rect x="0" y="8" width="14" height="1.5" fill="#fff"/></svg>
    Information Technology Services</div>
  <div class="svc-item" style="left:40px;top:460px">Enterprise Architecture</div>
  <div class="svc-item" style="left:40px;top:473px">Systems Engineering</div>
  <div class="svc-item" style="left:40px;top:486px">Business Process Engineering</div>
  <div class="svc-item" style="left:40px;top:500px">Software Engineering</div>
  <div class="svc-item" style="left:40px;top:513px">Cloud Computing/ Migration</div>

  <div class="svc-head" style="left:37px;top:532px">
    <svg width="16" height="10" viewBox="0 0 16 10" aria-hidden="true"><path d="M1 5h14M6 5l3-4M6 5l3 4M13 5l1-2" stroke="#fff" stroke-width="1.3" fill="none"/></svg>
    Aviation Services</div>
  <div class="svc-item" style="left:40px;top:555px">Air Traffic Program Management</div>
  <div class="svc-item" style="left:40px;top:569px;width:150px">Air Traffic Staffing Support i.e ZKA, ZKB, ZKC, ZKD</div>
  <div class="svc-item" style="left:40px;top:592px">UAS Policy and Procedures</div>
  <div class="svc-item" style="left:40px;top:605px">Commercial Space Transporation</div>
  <div class="svc-item" style="left:40px;top:618px">Safety and Feasiblity Studies</div>

  <div class="sec-head" style="left:248px;top:414px;width:237px"><span>Company Overview</span></div>
  <p class="overview">Skyvale Consulting Group, Inc. is a minority owned small business that provides strategic planning, and technology integration solutions for the Aviation and Aerospace community. Our strategic planning and technology expertise lies in the areas of Air Traffic Management, UAS Rules and Regulations, Cloud Migration, Cybersecurity, and Enterprise Architecture.</p>

  <div class="sec-head" style="left:248px;top:514px;width:237px"><span>Notable CFD Past Performances</span></div>
  <div class="list-item" style="left:248px;top:539px;width:240px">Eastern Shore Route Program Management Support (ESRP) - Airspace Services</div>
  <div class="list-item" style="left:248px;top:562px;width:240px">UAS Flight Authorization (UFA), and Records Request Approvals- Office of New Flight Tech</div>
  <div class="list-item" style="left:248px;top:585px;width:240px">National Airspace Enterprise Architecture- Joint Planning Team Office (JPTO)</div>
  <div class="list-item" style="left:248px;top:608px;width:240px">TeamDock Management &amp; Maintenance</div>

  <footer class="footer">
    <div class="footer__info">
      <svg width="7" height="7" viewBox="0 0 10 10" aria-hidden="true"><path d="M5 0L0 5h2v5h6V5h2z" fill="#fff"/></svg>
      48 Harbor Plaza Suite 300, Fairview MD 20900
      <span class="footer__sep"></span>
      <svg width="8" height="6" viewBox="0 0 8 6" aria-hidden="true"><rect x=".5" y=".5" width="7" height="5" fill="none" stroke="#fff"/><path d="M.5 .5L4 3.5 7.5 .5" fill="none" stroke="#fff"/></svg>
      martin.okafor@skyvaleconsulting.com
    </div>
    <div class="footer__phone">
      <svg width="11" height="11" viewBox="0 0 12 12" aria-hidden="true"><path d="M2.5 1l2 2.5-1 1.2a7 7 0 003.8 3.8l1.2-1 2.5 2-1.2 1.5C5 11 1 7 1 2.2z" fill="#fff"/></svg>
      (555) 014-2290
    </div>
  </footer>
</section>

<section class="page page--back">
  <div class="hero" role="img" aria-label="Silhouettes of business people shaking hands in an airport terminal with a control tower and aircraft beyond the windows"></div>
  <div class="brand">
    <div class="brand__name"><span class="brand__dot"></span>SKYVALE</div>
    <div class="brand__sub">CONSULTING GROUP</div>
  </div>

  <div class="panel" style="left:26px;top:258px;width:172px;height:374px"></div>
  <div class="tab" style="left:15px;top:266px;width:187px;height:25px;font-size:11.5px">PROFESSIONAL REFERENCES</div>

  <div class="ref" style="top:301px">Mr. Daniel Prescott<br>Coastal Flight Directorate,<br><b>Director</b>- Mission Support Services
    <div class="ref__mail"><span class="mail-ico"></span>Daniel.prescott@cfd.example</div></div>
  <div class="ref" style="top:370px">Mr. Colin Marsh<br>Coastal Flight Directorate<br><b>Manager</b>- Airspace Services
    <div class="ref__mail"><span class="mail-ico"></span>Colin.R.Marsh@cfd.example</div></div>
  <div class="ref" style="top:441px">Mr. Evan Lowry<br>Coastal Flight Directorate<br><b>Manager</b>- Maintenance Automation Team
    <div class="ref__mail"><span class="mail-ico"></span>Evan.lowry@cfd.example</div></div>

  <div class="photo" style="left:26px;top:514px;width:172px;height:118px" role="img" aria-label="Silhouette of a traveller with a suitcase watching an airliner through a blue-tinted terminal window"></div>

  <div class="sec-head" style="left:250px;top:270px;width:235px"><span>Why Hire us?</span></div>
  <div class="list-item sm" style="left:250px;top:294px;width:232px">Expert team of retired controllers with over 20 years of Air Traffic Control and Center Management experience</div>
  <div class="list-item sm" style="left:250px;top:318px;width:232px">Systems engineers with strong knowledge of ACQ-M Processes</div>
  <div class="list-item sm" style="left:250px;top:333px;width:232px">Experts in Cyber Security Policies and SISPA Compliance</div>
  <div class="list-item sm" style="left:250px;top:348px;width:232px">Experts in Enterprise Architecture frameworks such as DEFAF and EAF</div>
  <div class="list-item sm" style="left:250px;top:372px;width:232px">Experience performing UAS Integration feasibility studies and technology evaluation</div>
  <div class="list-item sm" style="left:250px;top:396px;width:232px">Coastal Transportation Fellows</div>
  <div class="list-item sm" style="left:250px;top:411px;width:232px">Competitive pricing and cost effective rates</div>

  <div class="sec-head" style="left:250px;top:431px;width:235px"><span>How to get to us?</span></div>
  <div class="list-item sm" style="left:250px;top:452px">FSA Schedule 70 (Prime)</div>
  <div class="list-item sm" style="left:372px;top:452px">eVANE (SubContractor)</div>
  <div class="list-item sm" style="left:250px;top:468px">CFD eQUICK (Prime)</div>
  <div class="list-item sm" style="left:372px;top:468px">SX2030 (Subcontractor)</div>

  <div class="sec-head" style="left:250px;top:497px;width:235px"><span>Our White Papers Publications</span></div>
  <div class="list-item sm" style="left:250px;top:522px;width:232px">Drones for Aid- A Study on effective use of Unmanned Aerial Systems during Disaster Relief</div>
  <div class="list-item sm" style="left:250px;top:546px;width:232px">SRDS-9, an alternative study of how to prevent runway incursion</div>
  <div class="list-item sm" style="left:250px;top:561px;width:232px">Drones Infra-Red Camera Technology- A study on how to use drones to facilitate crop dusting</div>
  <div class="list-item sm" style="left:250px;top:585px;width:232px">Cloud Computing- An acquisition strategy guide</div>
  <div class="list-item sm" style="left:250px;top:600px;width:232px">Cloud Migration Approach Best Practices</div>
  <div class="list-item sm" style="left:250px;top:615px;width:232px">Database Replication Pros and Cons</div>

  <footer class="footer">
    <div class="footer__info">
      <svg width="7" height="7" viewBox="0 0 10 10" aria-hidden="true"><path d="M5 0L0 5h2v5h6V5h2z" fill="#fff"/></svg>
      48 Harbor Plaza Suite 300, Fairview MD 20900
      <span class="footer__sep"></span>
      <svg width="8" height="6" viewBox="0 0 8 6" aria-hidden="true"><rect x=".5" y=".5" width="7" height="5" fill="none" stroke="#fff"/><path d="M.5 .5L4 3.5 7.5 .5" fill="none" stroke="#fff"/></svg>
      martin.okafor@skyvaleconsulting.com
    </div>
    <div class="footer__phone">
      <svg width="11" height="11" viewBox="0 0 12 12" aria-hidden="true"><path d="M2.5 1l2 2.5-1 1.2a7 7 0 003.8 3.8l1.2-1 2.5 2-1.2 1.5C5 11 1 7 1 2.2z" fill="#fff"/></svg>
      (555) 014-2290
    </div>
  </footer>
</section>

</body>
</html>
```